Alpine Friars Coffee: a new roasting company in Italy by real monks.

We need a logo and label design for a new coffee roastery in Italy, near Florence. We are real monks that roast coffee with wood. Very high quality. We would like to receive proposal for the logo "Alpine Friars coffee" design and labels. In the logo design a monk in black must be present but it must not be something serious or sad. The logo must have the writing "Alpine Friars coffee" more important and less important "Priory of Lanterns". We like something similar to the attached logo but the monk can also be seen in the face and more smiling. Italianness could be expressed on the labels but not banal (see Tuscan mountains). About the label: Our customers must first buy the beauty of the package and labels and then taste the coffee. It could be something particular like the attachment that we really like or something modern. The important thing is that the labels must be beautiful, even colorful but sober and elegant. Attached you will find the text on the front and back of the label. You can visit our web site www.prioratodellelanterne.it but the coffee is at the beginning, please visit our facebook https://www.facebook.com/www.eremodivalbrusca.org
IMPORTANT: We will not design the whole package but only a label on a neutral black package as attacched. What is important now is not the size of the package but the idea.
Now we just need an idea. The winner will be invited to a 1:1 job to perfect the labels of the 7 blends.

Target Market(s)

Retail

Industry/Entity Type

coffee

Requirements
Must have
• Monk design
Nice to have
• Something of special

```html
<!DOCTYPE html>
<html lang="en">
<head>
<meta charset="UTF-8">
<title>Alpine Friars Coffee – Brand &amp; Labels</title>
<link rel="stylesheet" href="https://fonts.googleapis.com/css2?family=Josefin+Sans:wght@400;700&family=Archivo+Narrow:wght@400;700&family=Oswald:wght@500&display=swap">
<style>
  :root {
    --paper: #ffffff;
    --maroon: #3a1d1f;
    --teal: #4faf9f;
    --teal-dark: #2f7a70;
    --salmon: #ee917a;
    --cream: #f4edd7;
    --leaf: #9fae8e;
    --berry: #d6714f;
    --ink: #231416;
    --white: #ffffff;
  }
  * { box-sizing: border-box; margin: 0; padding: 0; }
  html, body { width: 1200px; height: 720px; overflow: hidden; background: var(--paper); }
  body { position: relative; font-family: "Archivo Narrow", sans-serif; color: var(--ink); }

  /* Brand name block */
  .brand { position: absolute; left: 0; right: 0; top: 110px; display: flex; justify-content: center; align-items: center; gap: 18px; }
  .brand-dot { width: 56px; height: 56px; border-radius: 50%; background: var(--maroon); }
  .brand-name { font-family: "Archivo Narrow", sans-serif; font-weight: 700; font-size: 42px; color: var(--ink); line-height: 1; }

  /* Labels */
  .label { position: absolute; top: 300px; width: 420px; height: 390px; background: var(--maroon); overflow: hidden; }
  .label--front { left: 100px; }
  .label--back { left: 680px; }
  .label-art { position: absolute; left: 0; top: 0; width: 100%; height: 190px;
    background: radial-gradient(ellipse at 12% 30%, var(--leaf) 0 18%, transparent 40%),
                radial-gradient(ellipse at 88% 35%, var(--leaf) 0 16%, transparent 38%),
                radial-gradient(ellipse at 30% 15%, var(--berry) 0 10%, transparent 26%),
                radial-gradient(ellipse at 72% 18%, var(--berry) 0 9%, transparent 24%),
                var(--maroon); opacity: .85; }
  .label-shapes { position: absolute; left: 0; top: 0; }

  .label-brand { position: absolute; left: 0; right: 0; top: 100px; display: flex; justify-content: center; align-items: center; gap: 7px; }
  .label--back .label-brand { top: 58px; }
  .label-dot { width: 16px; height: 16px; border-radius: 50%; background: var(--white); }
  .label-name { font-family: "Archivo Narrow", sans-serif; font-weight: 700; font-size: 16px; color: var(--white); line-height: 1; }

  .front-desc { position: absolute; left: 30px; right: 30px; top: 140px; color: var(--white); font-size: 7.5px; line-height: 1.3; text-align: center; }
  .blend-name { position: absolute; left: 0; right: 0; top: 170px; text-align: center; color: var(--white); font-family: "Josefin Sans", sans-serif; font-size: 24px; font-weight: 400; letter-spacing: .5px; }

  .bean-type { position: absolute; left: 52px; top: 214px; display: flex; align-items: center; gap: 10px; color: var(--white); }
  .bean-type strong { font-family: "Josefin Sans", sans-serif; font-weight: 700; font-size: 25px; letter-spacing: 1px; }
  .bean-type .divider { width: 1.5px; height: 22px; background: var(--white); }
  .bean-type span { font-family: "Josefin Sans", sans-serif; font-size: 10px; line-height: 1; text-align: center; }

  .specs { position: absolute; left: 40px; right: 30px; top: 262px; display: grid; grid-template-columns: 1.2fr 1fr 1fr; text-align: center; font-family: "Josefin Sans", sans-serif; font-size: 11px; line-height: 1.15; }
  .specs div + div { border-left: 1.5px solid var(--ink); }
  .specs b { display: block; font-weight: 700; font-size: 12px; }

  .roast-scale { position: absolute; left: 46px; top: 299px; display: flex; align-items: center; gap: 6px; font-size: 7px; font-weight: 700; }
  .roast-bar { width: 250px; height: 10px; border: 1.2px solid var(--ink); background: var(--white); }
  .roast-bar i { display: block; width: 38%; height: 100%; background: var(--maroon); }

  .roast-note { position: absolute; left: 0; right: 0; top: 320px; text-align: center; font-family: "Josefin Sans", sans-serif; font-weight: 700; font-size: 11.5px; }

  .front-foot { position: absolute; left: 22px; right: 22px; top: 340px; height: 42px; }
  .fire-icon { position: absolute; left: 0; top: 4px; }
  .maker-line { position: absolute; left: 60px; width: 200px; top: 2px; text-align: center; font-size: 6.5px; line-height: 1.15; color: var(--white); }
  .url-pill { position: absolute; left: 98px; top: 26px; padding: 2px 12px; background: var(--white); border-radius: 8px; font-size: 7px; font-weight: 700; }
  .weight { position: absolute; right: 14px; top: 0; font-family: "Oswald", sans-serif; font-weight: 500; font-size: 15px; color: var(--white); }
  .made-in { position: absolute; right: 0; top: 24px; display: flex; align-items: center; gap: 3px; background: var(--white); padding: 2px 4px; font-size: 6px; font-weight: 700; line-height: 1; }
  .flag { display: flex; width: 18px; height: 11px; }
  .flag i { flex: 1; }
  .flag i:nth-child(1) { background: #1f8a4c; }
  .flag i:nth-child(2) { background: #f4f4f4; }
  .flag i:nth-child(3) { background: #cf2b37; }

  /* Back label */
  .story { position: absolute; left: 22px; right: 14px; top: 92px; height: 176px; background: var(--cream); padding: 8px 14px; text-align: center; color: var(--ink); }
  .story h2 { font-weight: 700; font-size: 9px; line-height: 1.15; margin-bottom: 5px; }
  .story p { font-size: 6.3px; line-height: 1.25; margin-bottom: 4px; }

  .back-info { position: absolute; left: 26px; top: 284px; width: 170px; text-align: center; font-size: 7px; line-height: 1.3; color: var(--white); }
  .storage-box { position: absolute; left: 200px; top: 282px; width: 100px; height: 82px; background: var(--white); }
  .storage-title { background: var(--ink); color: var(--white); font-size: 6px; font-weight: 700; padding: 3px 4px; }
  .best-before { font-size: 6.5px; padding: 3px 4px; }
  .eco-badge { position: absolute; left: 330px; top: 294px; width: 46px; height: 46px; border-radius: 50%; border: 2px solid var(--white); }
</style>
</head>
<body>

<header class="brand">
  <span class="brand-dot"></span>
  <span class="brand-name">Alpine Friars Coffee</span>
</header>

<section class="label label--front">
  <div class="label-art" role="img" aria-label="Illustrated coffee branches with green leaves and ripe red cherries"></div>
  <svg class="label-shapes" width="420" height="390" viewBox="0 0 420 390" aria-hidden="true">
    <path d="M0 208 C120 196 300 194 420 200 L420 390 L0 390 Z" fill="var(--teal)"/>
    <path d="M40 252 C20 256 0 260 0 264 L0 390 L420 390 L420 244 C300 248 120 250 40 252 Z" fill="var(--salmon)"/>
  </svg>
  <div class="label-brand"><span class="label-dot"></span><span class="label-name">Alpine Friars Coffee</span></div>
  <p class="front-desc">Indulge in our 100% Arabica coffee blend, featuring sweet, exotic fruit and spice notes,<br>medium-strong intensity, and lively citrus and floral hints of orange and bergamot.</p>
  <h1 class="blend-name">◆ THE AURORA BLEND ◆</h1>
  <div class="bean-type"><strong>ARABICA</strong><i class="divider"></i><span>100% WOOD<br>ROASTED COFFEE</span></div>
  <div class="specs">
    <div>PROCESS:<b>WOOD ROASTED</b></div>
    <div>REGION<b>TUSCANY</b></div>
    <div>REGION<b>HIGH</b></div>
  </div>
  <div class="roast-scale">LIGHT<div class="roast-bar"><i></i></div>DARK</div>
  <p class="roast-note">ROASTED TO ORDER, JUST BEFORE SHIPPING</p>
  <div class="front-foot">
    <svg class="fire-icon" width="22" height="26" viewBox="0 0 22 26" aria-hidden="true">
      <path d="M11 2 C15 8 17 11 16 15 C15 18 13 19 11 19 C8 19 6 17 6 14 C6 11 9 9 11 2 Z" fill="none" stroke="var(--white)" stroke-width="1.5"/>
      <path d="M3 20 L19 25 M19 20 L3 25" stroke="var(--white)" stroke-width="1.5"/>
    </svg>
    <p class="maker-line">ITALIAN HIGH QUALITY COFFEE<br>ROASTED BY THE FRIARS OF THE PRIORY<br>OF LANTERNS IN TUSCANY</p>
    <span class="url-pill">WWW.ALPINEFRIARS.COFFEE</span>
    <span class="weight">250 GR</span>
    <span class="made-in"><span class="flag"><i></i><i></i><i></i></span>MADE IN<br>ITALY</span>
  </div>
</section>

<section class="label label--back">
  <div class="label-art" role="img" aria-label="Illustrated coffee branches with green leaves and ripe red cherries"></div>
  <svg class="label-shapes" width="420" height="390" viewBox="0 0 420 390" aria-hidden="true">
    <path d="M0 150 L40 150 L40 268 L420 268 L420 390 L0 390 Z" fill="var(--teal)"/>
    <path d="M0 272 C140 262 300 264 420 266 L420 390 L0 390 Z" fill="var(--salmon)"/>
  </svg>
  <div class="label-brand"><span class="label-dot"></span><span class="label-name">Alpine Friars Coffee</span></div>
  <article class="story">
    <h2>Alpine Friars Coffee Blended and wood roasted in the<br>mountains near Florence by the Priory of Lanterns Friars</h2>
    <p>In their priory nestled deep in the Mugello mountains the friars blend and roast their coffee. The quiet meadows echo no sound but the occasional movements of a deer or a wild boar in the black pine forests. The song of a meadow lark welcomes the rising sun that lights up the mountain lake where a lonely ancient priory sits. The mountain peaks begin to twinkle orange in the bright morning sun. A gentle breeze plays with a peaceful cloud of what appears to be a typical mountain fog across the field before the priory. But it is not a fog. It is the delicious smoke of this morning's dark coffee roast.</p>
    <p>Every morning after prayers, a few of the friars walk down to their roasting barn whose yellow walls glimmer in the sunrise. They are ready to roast the coffee for today's blessed recipients. Curious about how our friars achieve their coffee mastery at 650 meters altitude in the picturesque Mugello mountains near Florence? Rest assured, our master roaster, with over 40 years of expertise, evokes the rich coffee traditions cherished by connoisseurs for fifteen years and beyond.</p>
  </article>
  <p class="back-info">Italian blend of roasted coffee beans<br>Produced and packaged by the Priory of<br>Lanterns - Eremo di Valbrusca - Tuscany<br>REA 04812395570<br>www.alpinefriars.coffee<br>www.lanternpriory.it<br>Net Weight 250 gr e 35.2 oz</p>
  <div class="storage-box">
    <div class="storage-title">KEEP IN A COOL AND DRY PLACE</div>
    <div class="best-before">Best before</div>
  </div>
  <div class="eco-badge"></div>
</section>

</body>
</html>
```